Pediatric Dentist Business Card

I need a business card designed for a dentist who works exclusively with children.
We prefer designs that are out of ordiary that is fun and interesting to kids.

there is no logo since this is a dentists office. The name of the doctor is "Tavor Kesh" if you want to get creative with that.

Target Market(s)

Kids

Industry/Entity Type

Business

Contact Information for Business Card

Anythings that is creative

Colors

Designer to choose colors to be used in the design.

```html
<!DOCTYPE html>
<html lang="en">
<head>
<meta charset="utf-8">
<title>Tavor Kesh — Pediatric Dentist Business Card</title>
<link href="https://fonts.googleapis.com/css2?family=Questrial&display=swap" rel="stylesheet">
<style>
  :root {
    --stage: #cbcbcb;
    --stage-edge: #555555;
    --purple: #4300a8;
    --orange: #f57a20;
    --white: #ffffff;
    --fruit-orange: #ffc48a;
    --fruit-pink: #f7b3d6;
    --fruit-purple: #d7b8f0;
    --fruit-yellow: #fbe98a;
    --fruit-green: #cfe9a4;
    --fruit-red: #f8a3a8;
  }
  * { box-sizing: border-box; margin: 0; padding: 0; }
  html, body { width: 1200px; height: 1186px; overflow: hidden; }
  body {
    background: var(--stage);
    border: 1px solid var(--stage-edge);
    font-family: "Questrial", sans-serif;
    position: relative;
  }
  .card {
    position: absolute;
    left: 242px;
    width: 696px;
    height: 397px;
    border-radius: 20px;
    overflow: hidden;
  }
  .card--front { top: 131px; background: var(--white); }
  .card--back { top: 670px; background: var(--purple); }

  .fruit-pattern {
    position: absolute; inset: 0;
    background:
      radial-gradient(circle at 6% 37%, var(--fruit-orange) 0 6%, transparent 10%),
      radial-gradient(circle at 12% 12%, var(--fruit-yellow) 0 5%, transparent 9%),
      radial-gradient(circle at 5% 67%, var(--fruit-yellow) 0 6%, transparent 10%),
      radial-gradient(circle at 12% 88%, var(--fruit-purple) 0 6%, transparent 10%),
      radial-gradient(circle at 28% 45%, var(--fruit-green) 0 5%, transparent 9%),
      radial-gradient(circle at 22% 80%, var(--fruit-orange) 0 5%, transparent 9%),
      radial-gradient(circle at 31% 8%, var(--fruit-pink) 0 5%, transparent 9%),
      radial-gradient(circle at 41% 22%, var(--fruit-orange) 0 5%, transparent 9%),
      radial-gradient(circle at 38% 70%, var(--fruit-green) 0 5%, transparent 9%),
      radial-gradient(circle at 45% 85%, var(--fruit-pink) 0 6%, transparent 10%),
      radial-gradient(circle at 56% 88%, var(--fruit-orange) 0 6%, transparent 10%),
      radial-gradient(circle at 57% 19%, var(--fruit-pink) 0 6%, transparent 10%),
      radial-gradient(circle at 68% 33%, var(--fruit-pink) 0 6%, transparent 10%),
      radial-gradient(circle at 66% 85%, var(--fruit-purple) 0 6%, transparent 10%),
      radial-gradient(circle at 74% 12%, var(--fruit-red) 0 3%, transparent 6%),
      radial-gradient(circle at 79% 22%, var(--fruit-yellow) 0 6%, transparent 10%),
      radial-gradient(circle at 77% 66%, var(--fruit-yellow) 0 6%, transparent 10%),
      radial-gradient(circle at 88% 17%, var(--fruit-red) 0 3%, transparent 6%),
      radial-gradient(circle at 91% 37%, var(--fruit-orange) 0 6%, transparent 10%),
      radial-gradient(circle at 85% 55%, var(--fruit-yellow) 0 6%, transparent 10%),
      radial-gradient(circle at 93% 62%, var(--fruit-yellow) 0 5%, transparent 9%),
      radial-gradient(circle at 86% 88%, var(--fruit-green) 0 7%, transparent 11%),
      linear-gradient(135deg, #fffaf4, #fdf6fb 50%, #f9fcf2);
    opacity: 0.85;
  }
  .front-brand {
    position: absolute;
    left: 0; right: 0; top: 196px;
    display: flex; justify-content: center; align-items: center; gap: 12px;
  }
  .brand-dot { width: 24px; height: 24px; border-radius: 50%; background: var(--orange); }
  .front-brand .brand-name {
    font-size: 36px; color: var(--purple);
    background: var(--white); padding: 4px 16px; border-radius: 30px;
  }

  .name-band {
    position: absolute;
    left: 0; top: 65px;
    width: 335px; height: 55px;
    background: var(--white);
    display: flex; align-items: center; justify-content: flex-end;
    padding-right: 24px;
  }
  .doctor-name { font-size: 32px; font-weight: 400; color: var(--purple); }

  .contact-list {
    position: absolute; left: 70px; top: 174px;
    list-style: none;
  }
  .contact-list li {
    display: flex; align-items: center; gap: 13px;
    height: 37.5px;
    font-size: 21px; color: var(--white); letter-spacing: 0.3px;
  }
  .contact-icon { width: 20px; height: 20px; flex: none; }

  .back-brand {
    position: absolute; right: 26px; bottom: 18px;
    display: flex; align-items: center; gap: 8px;
  }
  .back-brand .brand-dot { width: 16px; height: 16px; }
  .back-brand .brand-name { font-size: 24px; color: var(--orange); }
</style>
</head>
<body>

  <section class="card card--front">
    <div class="fruit-pattern" role="img" aria-label="Bright pastel pattern of assorted fruits: oranges, berries, bananas, cherries, melons and kiwis"></div>
    <div class="front-brand">
      <span class="brand-dot"></span>
      <span class="brand-name">Tavor Kesh</span>
    </div>
  </section>

  <section class="card card--back">
    <div class="name-band">
      <h1 class="doctor-name">Dr. Tavor Kesh</h1>
    </div>

    <ul class="contact-list">
      <li>
        <svg class="contact-icon" viewBox="0 0 20 20" fill="#ffffff" aria-hidden="true">
          <path d="M2 7c0-2 3.5-3.5 8-3.5S18 5 18 7v1.5h-4V6.8c-1.2-.4-2.6-.6-4-.6s-2.8.2-4 .6v1.7H2z"/>
          <path d="M4.5 10l2-2.5h7l2 2.5v6h-11z"/>
        </svg>
        <span>(555) 018-2946</span>
      </li>
      <li>
        <svg class="contact-icon" viewBox="0 0 20 20" fill="none" stroke="#ffffff" stroke-width="1.8" aria-hidden="true">
          <rect x="2" y="4.5" width="16" height="11" rx="1"/>
          <path d="M2 5l8 6 8-6M2 15l6-5M18 15l-6-5"/>
        </svg>
        <span>tavor@brightsmilekids.com</span>
      </li>
      <li>
        <svg class="contact-icon" viewBox="0 0 20 20" fill="none" stroke="#ffffff" stroke-width="1.5" aria-hidden="true">
          <circle cx="10" cy="10" r="8"/>
          <ellipse cx="10" cy="10" rx="3.5" ry="8"/>
          <path d="M2 10h16M3.5 6h13M3.5 14h13"/>
        </svg>
        <span>www.brightsmilekids.com</span>
      </li>
    </ul>

    <div class="back-brand">
      <span class="brand-dot"></span>
      <span class="brand-name">Tavor Kesh</span>
    </div>
  </section>

</body>
</html>
```